Web Design Project

We need the homepage and 7 interior pages designed as described below - design only:

Main Page
We like this template: http://www.layoutbarn.example/demo/52917.html

We also want a login dropdown similar to http://www.vortelle.example

We want the main page to be luxurious and sleek. We are a limo company that is dedicated to good service and creating an experience, and our front page should strongly reflect that. We do not want a very busy front page.

The main page should do primary things:

1. Make Reservations: We really like rideharbor.example for this aspect of the site. That being said, rideharbor is NOT the type of company we are.
2. Inform the customer of our most popular packages and give a sense of our professionalism and luxurious service.
3. There should be an area for a customer login
4. Menu should include the following: Home, Who We Are, Our Fleet, Custom Packages,
Testimonials, Book Your Ride!

For a starting point, we like this template http://www.layoutbarn.example/demo/52917.html

Rather than "start up, integrate, develop" we could have 3 of the more popular packages (or categories of packages). The bottom part would be fine. We could have a chirpline feed, welcome, and our core principles. The one big change would be the addition of a "booking" area right smack in the middle of the page, where a customer could enter in trip data and see if the date was available.

-

About Us - Secondary Page
We like this ABOUT page template: http://www.layoutbarn.example/demo/63824.html

This is a really important page that people overlook, yet it is the most viewed page of a website after the homepage. We have come up with a bit of text to go on the about us page:

Who We Are: Velvet Cars was founded on the core principle that every limo ride starts with personalized service from the instant you book your ride and continues after you step out of the car. You and your party are more than just our customers. We consider knowing your name and providing you with your choice of snacks and periodicals in the car just a few of the integral elements of the limousine experience. We are striving to revolutionize the limousine industry by creating a personal, friendly, timely, and professional experience. Velvet Cars combines current technology and a modern fleet with good old-fashioned service to deliver you a personalized, luxury experience. We cater to every event, from business travel to proms and wedding, and everything in between.

We do all of this while maintaining competitive pricing to our peers.

Have a taste of high society...

-

Custom Packages - Secondary Page

This page will contain descriptions of the packages that we offer: Wedding, Prom, Business, etc. - there should be a thumbnail of each package with a description next to it. When you click on a thumbnail it will bring you to a detailed page of that particular package.

-

Custom Packages Interior Page - Secondary Page

In depth look at that particular package - for example, weddings - shows that we offer complimentary champagne, Just married sign, etc.

-

Fleet Page - Secondary Page

This page can be fairly basic. It will include photos of the vehicles along with descriptions and number of passengers, etc.

-

Testimonials Page - Secondary Page

This page will have testimonials from customers. We don't want a big block of text, but rather small testimonials that will expand within the page when you click on a "+" symbol. We like the way it looks when the testimonials are enclosed within a speech bubble image - still professional and classy, not cheesy.

-

Book your ride! - Secondary Page

This page will have a form on it - the same as the form on the homepage, where people can enter in information to check the availability of vehicles. We also want basic contact information on this page as well in case people want to call directly or e-mail.

Requirements
Must have
• - Book your reservation form on homepage
- Sleek, elegant feel
- Chirpline feed

```html
<!DOCTYPE html>
<html lang="en">
<head>
<meta charset="utf-8">
<title>Velvet Cars – Who We Are</title>
<link href="https://fonts.googleapis.com/css2?family=Arimo:ital,wght@0,400;0,700;1,400&display=swap" rel="stylesheet">
<style>
:root{
  --edge:#232323;
  --page:#2d2d2d;
  --panel:#262626;
  --panel-dark:#222;
  --heading:#dcdcdc;
  --text:#a9a9a9;
  --faint:#555;
  --blue:#1b9ad8;
  --nav-active-top:#0c66bf;
  --nav-active-bottom:#0a4a92;
  --rule:#4a4a4a;
  --photo-cool:#b9bcc0;
  --photo-warm:#c9a58a;
}
*{box-sizing:border-box;margin:0;padding:0}
html,body{width:870px;height:1200px;overflow:hidden}
body{background:var(--edge);font-family:"Arimo",Arial,sans-serif;color:var(--text);position:relative}
.page{position:absolute;left:57px;top:0;width:756px;height:1200px;background:var(--page)}
.abs{position:absolute}

.account{left:594px;top:0;width:157px;height:39px;background:var(--panel-dark);display:flex}
.account a{flex:1;display:flex;align-items:center;justify-content:center;color:#e6e6e6;font-size:11px;text-decoration:none}
.account a + a{border-left:1px solid #3a3a3a}

.brand{left:119px;top:56px;color:#cfcfcf;font-size:22px;font-weight:400;line-height:1}
.tollfree{right:117px;top:72px;color:#d8d8d8;font-size:9.5px}

.main-nav{left:113px;top:106px;width:639px;height:53px;background:var(--panel);display:flex}
.main-nav a{display:flex;align-items:center;justify-content:center;color:#e8e8e8;font-size:10.5px;font-weight:700;text-decoration:none;border-right:1px solid #2f2f2f}
.main-nav a:last-child{border-right:0}
.main-nav .is-active{background:linear-gradient(var(--nav-active-top),var(--nav-active-bottom))}

.section-title{color:var(--heading);font-size:22px;font-weight:700;line-height:1}

.about-frame{left:116px;top:247px;width:210px;height:154px;background:var(--panel)}
.about-photo{left:127px;top:258px;width:189px;height:133px;background:linear-gradient(120deg,#6b5446 0%,#8a7a70 35%,var(--photo-cool) 60%,#e9e9e9 100%)}
.about-copy{left:347px;top:247px;width:406px;font-size:9.2px;line-height:12.75px;text-align:justify}
.about-copy p + p{margin-top:12.75px}

.service{left:122px;width:360px}
.service .tick{position:absolute;left:0;top:0;width:19px;height:19px}
.service h3{position:absolute;left:31px;top:1px;color:var(--blue);font-size:12px;font-weight:700;white-space:nowrap}
.service p{position:absolute;left:32px;top:19px;width:330px;font-size:8.2px;line-height:12.6px;color:#c4c4c4}
.dash{height:0;border-top:1px dashed var(--rule)}

.quote-box{left:532px;top:499px;width:221px;height:110px;background:var(--panel);padding:15px 13px;font-style:italic;font-size:9.4px;line-height:14.3px;text-align:justify;color:#a4a4a4}
.quote-tail{left:548px;top:608px}
.author-frame{left:532px;top:632px;width:107px;height:81px;background:var(--panel)}
.author-photo{left:539px;top:639px;width:93px;height:67px;background:linear-gradient(135deg,#e4e6e8,var(--photo-warm) 55%,#5a4a40)}
.author-name{left:654px;top:657px;color:#e0e0e0;font-size:11px;font-weight:700}
.author-role{left:654px;top:674px;color:var(--blue);font-size:9.5px}

.pager{top:779px;width:19px;height:18px;background:#242424;display:flex;align-items:center;justify-content:center;color:#ddd;font-size:10px}

.team{left:120px;top:825px;width:633px;height:202px;background:#292929;border-top:1px solid #111;border-left:1px solid #111}
.member{top:27px;width:120px}
.member .portrait{width:93px;height:93px;background:linear-gradient(160deg,#f2f2f2 0%,var(--photo-warm) 55%,#6d5444 100%)}
.member h4{margin-top:17px;color:var(--blue);font-size:9.8px;font-weight:700;white-space:nowrap}
.member p{margin-top:6px;width:100px;font-size:8.3px;line-height:10.6px;color:#8e8e8e}

.foot-rule{left:113px;top:1098px;width:635px}
.to-top{left:773px;top:1086px;width:36px;height:36px;background:#262626;color:var(--blue);font-size:11px;display:flex;align-items:center;justify-content:center}
.foot-brand{left:114px;top:1142px;color:#bdbdbd;font-size:15px;font-weight:400;line-height:1}
.legal{left:264px;top:1146px;color:var(--faint);font-size:8px}
.social{left:620px;top:1141px;display:flex;gap:6px}
.social span{width:15px;height:15px;border-radius:50%;background:#cfcfcf;display:block}
</style>
</head>
<body>
<div class="page"></div>

<nav class="abs account"><a href="#">LOGIN</a><a href="#">REGISTER</a></nav>

<div class="abs brand">Velvet Cars</div>
<div class="abs tollfree">CALL US TOLL FREE 1-555-014-27-60</div>

<nav class="abs main-nav">
  <a href="#" style="width:106px">HOME</a>
  <a href="#" class="is-active" style="width:112px">WHO WE ARE</a>
  <a href="#" style="width:95px">OUR FLEET</a>
  <a href="#" style="width:119px">CUSTOM PACKAGES</a>
  <a href="#" style="width:99px">TESTIMONIALS</a>
  <a href="#" style="width:108px">BOOK YOUR RIDE!</a>
</nav>

<h1 class="abs section-title" style="left:123px;top:204px">WHO WE ARE</h1>
<div class="abs about-frame"></div>
<div class="abs about-photo" role="img" aria-label="Chauffeur in a dark suit standing beside a white stretch limousine on a city street"></div>
<div class="abs about-copy">
  <p>Velvet Cars was founded on the core principle that every limo ride starts with personalized service from the instant you book your ride and continues after you step out of the car. You and your party are more than just our customers. We consider knowing your name and providing you with your choice of snacks and periodicals in the car just a few of the integral elements of the limousine experience. We are striving to revolutionize the limousine industry by creating a personal, friendly, timely, and professional experience. Velvet Cars combines current technology and a modern fleet with good old-fashioned service to deliver you a personalized, luxury experience. We cater to every event, from business travel to proms and wedding, and everything in between.</p>
  <p>We do all of this while maintaining competitive pricing to our peers.</p>
  <p>Have a taste of high society...</p>
</div>

<h2 class="abs section-title" style="left:123px;top:460px">WHAT WE DO</h2>

<div class="abs service" style="top:499px">
  <svg class="tick" viewBox="0 0 19 19"><circle cx="9.5" cy="9.5" r="9.5" fill="#1c1c1c"/><path d="M5.5 9.8l2.6 2.8 5.2-6.2" fill="none" stroke="#eee" stroke-width="1.8"/></svg>
  <h3>LOREM IPSUM PRAETIU PTATUM DELENITIMAT</h3>
  <p>Eiart urie ntots nascetur riculus mulla dugilead ravida atcurus necu a lorem accumsan maleuada orcic sit amet em ipsumdolor sit amt consc.</p>
</div>
<div class="abs dash" style="left:122px;top:561px;width:360px"></div>

<div class="abs service" style="top:575px">
  <svg class="tick" viewBox="0 0 19 19"><circle cx="9.5" cy="9.5" r="9.5" fill="#1c1c1c"/><path d="M5.5 9.8l2.6 2.8 5.2-6.2" fill="none" stroke="#eee" stroke-width="1.8"/></svg>
  <h3>LOREM IPSUM PRAETIU PTATUM DELENITIMAT</h3>
  <p>Eiart urie ntots nascetur riculus mulla dugilead ravida atcurus necu a lorem accumsan maleuada orcic sit amet em ipsumdolor sit amt consc.</p>
</div>
<div class="abs dash" style="left:122px;top:637px;width:360px"></div>

<div class="abs service" style="top:651px">
  <svg class="tick" viewBox="0 0 19 19"><circle cx="9.5" cy="9.5" r="9.5" fill="#1c1c1c"/><path d="M5.5 9.8l2.6 2.8 5.2-6.2" fill="none" stroke="#eee" stroke-width="1.8"/></svg>
  <h3>LOREM IPSUM PRAETIU PTATUM DELENITIMAT</h3>
  <p>Eiart urie ntots nascetur riculus mulla dugilead ravida atcurus necu a lorem accumsan maleuada orcic sit amet em ipsumdolor sit amt consc.</p>
</div>
<div class="abs dash" style="left:122px;top:713px;width:360px"></div>

<h2 class="abs section-title" style="left:532px;top:460px">TESTIMONIALS</h2>
<blockquote class="abs quote-box">“ Ut te dolor dapibus eget elentu vclend elit. Aenean auctorlutpat. Duis tur uest um liberoisl porta vel sceleisaluada at neque. Vivam nibhus leo velaenean nec eros. Vestibulum ante ipsum. ”</blockquote>
<svg class="abs quote-tail" width="20" height="17" viewBox="0 0 20 17"><path d="M0 0h20L18 17z" fill="#262626"/></svg>
<div class="abs author-frame"></div>
<div class="abs author-photo" role="img" aria-label="Portrait of the customer giving the testimonial"></div>
<div class="abs author-name">SAL KERWINTER</div>
<div class="abs author-role">Lorem Ipsum Dolor</div>

<h2 class="abs section-title" style="left:123px;top:772px">MEET OUR TEAM</h2>
<div class="abs pager" style="left:712px">&lsaquo;</div>
<div class="abs pager" style="left:734px">&rsaquo;</div>

<section class="abs team">
  <div class="abs member" style="left:30px"><div class="portrait" role="img" aria-label="Portrait of Marco Delane"></div><h4>MARCO DELANE</h4><p>Gravida atem cursus nec luctus lorem maecenas.</p></div>
  <div class="abs member" style="left:151px"><div class="portrait" role="img" aria-label="Portrait of Brent Halloway"></div><h4>BRENT HALLOWAY</h4><p>Gravida atem cursus nec luctus lorem maecenas.</p></div>
  <div class="abs member" style="left:271px"><div class="portrait" role="img" aria-label="Portrait of Janna Pruitt"></div><h4>JANNA PRUITT</h4><p>Gravida atem cursus nec luctus lorem maecenas.</p></div>
  <div class="abs member" style="left:392px"><div class="portrait" role="img" aria-label="Portrait of Oriana Fenwick"></div><h4>ORIANA FENWICK</h4><p>Gravida atem cursus nec luctus lorem maecenas.</p></div>
  <div class="abs member" style="left:511px"><div class="portrait" role="img" aria-label="Portrait of Lena Sorrell"></div><h4>LENA SORRELL</h4><p>Gravida atem cursus nec luctus lorem maecenas.</p></div>
</section>

<div class="abs dash foot-rule"></div>
<div class="abs to-top">TOP</div>
<div class="abs foot-brand">Velvet Cars</div>
<div class="abs legal">© COPYRIGHT 2012 | ALL RIGHTS RESERVED | PRIVACY POLICY</div>
<div class="abs social" aria-label="Social links"><span role="img" aria-label="Chirpline"></span><span role="img" aria-label="Social network"></span><span role="img" aria-label="News feed"></span></div>
</body>
</html>
```